Designing a brochures for an educational counseling service provider

We would like a 4 sided design on a 11x8.5 paper, half folded. I have including a sample design we did to give you an idea of what we envision but we welcome creativity to make beautiful looking flyers. Text for the flier is included as well as our logo.
- The most important thing is capturing our audience/market. We will be handing these flies to schools, organizations and individual clients.

www.plorvaeducationalconsultants.example

Target Market(s)

We are targeting international students wanting to study in the U.S and Canada.

Industry/Entity Type

Education

Requirements
Must have
• - Clean and clear
• - Our logo should visible and well placed.
• - Could you the pictures of students, libraries and school buildings or you could use the pictures we already have.
Nice to have
• We would like this to match business cards.

```html
<!DOCTYPE html>
<html lang="en">
<head>
<meta charset="utf-8">
<title>Plorva Educational Consultants Brochure</title>
<link href="https://fonts.googleapis.com/css2?family=Lato:wght@400;700;900&family=Michroma&family=Oswald:wght@600&display=swap" rel="stylesheet">
<style>
  :root{
    --navy:#0d3f8f;
    --blue:#1a5cb8;
    --sky:#2c8ad8;
    --green:#7ed321;
    --lime:#a6e22e;
    --ink:#1d2a4a;
    --paper:#ffffff;
    --stage:#e9ecef;
  }
  *{margin:0;padding:0;box-sizing:border-box}
  html,body{width:1200px;height:848px;overflow:hidden;background:var(--stage)}
  .spread{position:absolute;left:82px;top:24px;width:1036px;height:800px;display:flex;box-shadow:0 6px 24px rgba(0,0,0,.18)}
  .page{position:relative;width:518px;height:800px;background:var(--paper);overflow:hidden;font-family:"Lato",sans-serif}
  .page svg.bg{position:absolute;inset:0}
  .call{position:absolute;right:30px;top:64px;text-align:right;color:var(--navy);font-family:"Michroma",sans-serif}
  .call .label{font-size:16px}
  .call .phone{font-size:18px;color:var(--sky);margin-top:6px}
  .about{position:absolute;left:34px;top:392px;width:446px;color:var(--ink)}
  .about h2{font-family:"Michroma",sans-serif;font-size:18px;color:var(--sky);margin-bottom:10px}
  .about p{font-size:13px;font-weight:700;line-height:1.32;text-align:justify;margin-bottom:10px}
  .brand{display:flex;align-items:center;gap:8px;font-family:"Lato",sans-serif;font-weight:900;color:var(--blue)}
  .brand .dot{border-radius:50%;background:var(--green)}
  .back-brand{position:absolute;right:40px;top:636px;font-size:26px}
  .back-brand .dot{width:20px;height:20px}
  .contact{position:absolute;left:34px;top:684px;color:var(--navy);font-size:12.5px;font-weight:700}
  .contact .email a{color:var(--sky);text-decoration:none}
  .contact .web{font-size:14px;margin-top:4px}
  .front-brand{position:absolute;left:40px;top:40px;font-size:34px}
  .front-brand .dot{width:28px;height:28px}
  .tagline{position:absolute;left:0;right:0;top:622px;text-align:center;color:#fff}
  .tagline .l1{font-family:"Michroma",sans-serif;font-size:17px}
  .tagline .l2{font-family:"Michroma",sans-serif;font-size:14px;color:var(--lime);margin-top:6px}
  .tagline .l3{font-family:"Oswald",sans-serif;font-size:29px;margin-top:4px;letter-spacing:.3px}
  .tagline .web{font-size:12px;letter-spacing:4px;margin-top:14px;font-weight:700}
</style>
</head>
<body>
<div class="spread">
  <section class="page back-page">
    <svg class="bg" width="518" height="800" viewBox="0 0 518 800">
      <defs>
        <radialGradient id="libraryPhoto" cx="50%" cy="45%" r="60%">
          <stop offset="0" stop-color="#b88a6a"/>
          <stop offset="1" stop-color="#4a3b3a"/>
        </radialGradient>
      </defs>
      <path d="M120 322 C260 330 400 290 518 318 L518 332 C400 306 260 346 110 334Z" fill="var(--green)"/>
      <circle cx="150" cy="190" r="128" fill="none" stroke="var(--navy)" stroke-width="10"/>
      <circle cx="150" cy="190" r="119" fill="url(#libraryPhoto)" role="img" aria-label="Photo of three students reading together in a library"/>
      <path d="M0 745 C170 775 350 750 518 680 L518 800 L0 800Z" fill="var(--green)"/>
      <path d="M0 765 C175 790 355 765 518 700 L518 800 L0 800Z" fill="#fff"/>
      <path d="M0 778 C180 800 360 778 518 712 L518 800 L0 800Z" fill="var(--lime)"/>
      <path d="M80 800 C260 792 410 760 518 725 L518 800Z" fill="var(--navy)"/>
    </svg>
    <div class="call"><div class="label">CALL US NOW:</div><div class="phone">555-014-2290</div></div>
    <div class="about">
      <h2>ABOUT US:</h2>
      <p>Our mission is to make quality education accessible and affordable to the families we serve. Our services are designed with the child's future in mind. Whether one is seeking an academic or non-academic environment, it is important to us that we set our clients up for success.</p>
      <p>We are a family-centered organization and our goals are the same as those of our clients; for their child to thrive and reach their goals and dreams. With over 10 years of experience in the business, we are aware of the financial obstacles created by the ever increasing cost in education. Our expert consultants work closely with families to map out their educational budget and find the best affordable and quality educational options.</p>
    </div>
    <div class="brand back-brand"><span class="dot"></span>Plorva</div>
    <div class="contact">
      <div class="email">Email: <a href="mailto:hello@plorvaeducationalconsultants.example">hello@plorvaeducationalconsultants.example</a></div>
      <div class="web">www.plorvaeducationalconsultants.example</div>
    </div>
  </section>

  <section class="page front-page">
    <svg class="bg" width="518" height="800" viewBox="0 0 518 800">
      <defs>
        <linearGradient id="studentsPhoto" x1="0" y1="0" x2="1" y2="1">
          <stop offset="0" stop-color="#6b4a3a"/>
          <stop offset=".5" stop-color="#3a2a26"/>
          <stop offset="1" stop-color="#8a6a5a"/>
        </linearGradient>
        <linearGradient id="navyBand" x1="0" y1="0" x2="0" y2="1">
          <stop offset="0" stop-color="var(--blue)"/>
          <stop offset="1" stop-color="var(--navy)"/>
        </linearGradient>
      </defs>
      <path d="M150 112 C300 92 430 70 518 40 L518 60 C420 100 300 118 170 122Z" fill="var(--green)"/>
      <path d="M0 150 C200 120 380 110 518 70 L518 520 C380 560 200 560 0 480Z" fill="url(#studentsPhoto)" role="img" aria-label="Photo of three smiling students standing together"/>
      <path d="M0 480 C200 560 380 560 518 520 L518 540 C380 585 200 585 0 500Z" fill="var(--green)"/>
      <path d="M0 512 C200 596 380 596 518 552 L518 800 L0 800Z" fill="url(#navyBand)"/>
    </svg>
    <div class="brand front-brand"><span class="dot"></span>Plorva</div>
    <div class="tagline">
      <div class="l1">A full-service international</div>
      <div class="l2">educational consulting group serving</div>
      <div class="l3">students and families across the globe</div>
      <div class="web">www.plorvaeducationalconsultants.example</div>
    </div>
  </section>
</div>
</body>
</html>
```